Software Specialist in Artificial Intelligence innovation needs a smart and professional looking bus

Prefers a clean and professional design, yet portraying a class of its own and a world-class feel. We develop state-of-the-art software automation engines by deploying artificial intelligence that simulates the smartest brains that are able to simulate a human consultant and/or data scientist. Both single-sided or double-sided design is acceptable. Do not refer too much to our current website as we are also in the process of revamping it so that it better reflects who we are and what we do.
Updates

Project Deadline Extended
Reason: A substantial number of designs submitted to date deviates a fair bit from requirements and expectations. Feedbacks will be provided to all parties by today and as such, an extension is catered to accomodate re-submissions.

Target Market(s)

Software technology companies, software developers, enterprise clients that requires automation supported by Artificial Intelligence driven software solutions.

Industry/Entity Type

Software

Contact Information for Business Card

Marcus Tan
Chief Innovator
marcustan@veltrixia.com
mobile: +65 94567312
Company Name: Veltrixia Pte Ltd
Address: 14 Sorbank Road #05-11 Harlowe Point, Singapore 538422
Telephone: +65 63417250
Website: www.Veltrixia.com
Please do not include the titles of the above fields.

Font styles to use
Sans Serif
Other font styles liked:
• Calibri, Futura Condensed

Requirements
Must have
• Portrays a professional and innovative image. Should reflect that the company is into Artificial Intelligence software development, high tech kind of feel.
Nice to have
• A plus point would be if you can even come up with a new company logo for us, representing who we are. Our current company logo is attached.
Should not have
• Fanciful stuffs as it must portray a professional image. Prefers not to have the cloud "image" as part of the logo or in the name card.

```html
<!DOCTYPE html>
<html lang="en">
<head>
<meta charset="utf-8">
<title>Veltrixia – Business Card</title>
<link rel="stylesheet" href="https://fonts.googleapis.com/css2?family=Didact+Gothic&family=Questrial&display=swap">
<style>
  :root {
    --canvas-bg: #e6e4e1;
    --card-white: #f4f4f3;
    --panel-dark: #3f3f42;
    --accent-red: #a3343a;
    --ink-dark: #3d3d40;
    --ink-grey: #8a8a8c;
    --panel-text: #b9b9bb;
    --panel-text-soft: #a6a6a8;
  }
  * { margin: 0; padding: 0; box-sizing: border-box; }
  html, body {
    width: 1200px; height: 720px; overflow: hidden;
    background: var(--canvas-bg);
  }
  .canvas {
    width: 1200px; height: 720px;
    display: flex; align-items: center; justify-content: center;
  }
  .card {
    position: relative;
    width: 1050px; height: 600px;
    background: var(--card-white);
    overflow: hidden;
    box-shadow: 0 6px 20px rgba(0,0,0,0.12);
  }
  .card__shapes { position: absolute; inset: 0; }
  .brand {
    position: absolute; left: 64px; top: 128px;
    display: flex; align-items: center; gap: 18px;
  }
  .brand__mark {
    width: 64px; height: 64px; background: var(--accent-red);
  }
  .brand__name {
    font-family: "Questrial", sans-serif;
    font-size: 50px; color: var(--ink-dark); letter-spacing: 0.5px;
  }
  .website {
    position: absolute; left: 150px; top: 432px;
    font-family: "Didact Gothic", sans-serif;
    font-size: 26px; color: var(--ink-grey);
  }
  .website__name { color: var(--ink-dark); font-family: "Questrial", sans-serif; }
  .contact {
    position: absolute; right: 56px; top: 74px;
    text-align: right;
    font-family: "Didact Gothic", sans-serif;
    color: var(--panel-text);
  }
  .contact__name { font-size: 54px; line-height: 1.05; }
  .contact__title { font-size: 27px; color: var(--panel-text-soft); margin-bottom: 40px; }
  .contact__list { list-style: none; font-size: 23px; line-height: 1.7; }
  .contact__item { display: flex; align-items: center; justify-content: flex-end; gap: 14px; }
  .contact__icon { width: 22px; height: 22px; flex: none; }
  .contact__item--plain { padding-right: 36px; }
</style>
</head>
<body>
<main class="canvas">
  <section class="card">
    <svg class="card__shapes" width="1050" height="600" viewBox="0 0 1050 600" aria-hidden="true">
      <path d="M455 0 C 430 170, 440 400, 515 600 L1050 600 L1050 0 Z" fill="var(--accent-red)"/>
      <path d="M500 0 C 452 180, 462 420, 528 600 L1050 600 L1050 0 Z" fill="var(--panel-dark)"/>
    </svg>

    <div class="brand">
      <span class="brand__mark"></span>
      <span class="brand__name">Veltrixia</span>
    </div>

    <p class="website">www.<span class="website__name">Veltrixia</span>.com</p>

    <div class="contact">
      <h1 class="contact__name">Marcus Tan</h1>
      <p class="contact__title">Chief Innovator</p>
      <ul class="contact__list">
        <li class="contact__item">marcustan@veltrixia.com
          <svg class="contact__icon" viewBox="0 0 22 22" fill="none" stroke="var(--panel-text)" stroke-width="1.5"><rect x="2" y="5" width="18" height="12"/><path d="M2 5 L11 12 L20 5 M2 17 L9 11 M20 17 L13 11"/></svg>
        </li>
        <li class="contact__item">+ 65 945 67312
          <svg class="contact__icon" viewBox="0 0 22 22" fill="none" stroke="var(--panel-text)" stroke-width="1.5"><rect x="6" y="2" width="10" height="18" rx="1.5"/><rect x="8" y="4" width="6" height="5"/><path d="M8 12h6M8 14.5h6M8 17h6"/></svg>
        </li>
        <li class="contact__item">+ 65 634 17250
          <svg class="contact__icon" viewBox="0 0 22 22" fill="var(--panel-text)"><path d="M2 9 C2 5 20 5 20 9 L17 10.5 L15 8 L7 8 L5 10.5 Z"/><path d="M6 12 L16 12 L18 18 L4 18 Z"/></svg>
        </li>
        <li class="contact__item">14 Sorbank Road #05-11
          <svg class="contact__icon" viewBox="0 0 22 22" fill="var(--panel-text)"><path d="M11 2 C6.5 2 4 5.5 4 9 C4 13.5 11 20 11 20 C11 20 18 13.5 18 9 C18 5.5 15.5 2 11 2 Z M11 6.5 A2.5 2.5 0 1 1 11 11.5 A2.5 2.5 0 1 1 11 6.5 Z" fill-rule="evenodd"/></svg>
        </li>
        <li class="contact__item contact__item--plain">Harlowe Point, Singapore</li>
      </ul>
    </div>
  </section>
</main>
</body>
</html>
```